Electrician Needs A Business Card

I already have a logo and would like a business card to be designed based around this logo the company is called Tolvane Electrical Pty Ltd

The business card will be printed on transparent plastic so I need it to stand out from the crowd. I do not want the card to have anything to do with Electrical on it eg light bulbs, power points etc

I need it to have the following details.

Gareth Pomfrey
Mobile : 0437 519 284
email : gareth@tolvaneelectrical.com.au

If it could incorporate the following onto the bottom of the card
ELECTRICAL - COMMUNICATIONS - AUDIO - VISUAL

```html
<!DOCTYPE html>
<html lang="en">
<head>
<meta charset="utf-8">
<title>Tolvane Electrical – Business Card</title>
<link rel="stylesheet" href="https://fonts.googleapis.com/css2?family=Arimo:wght@400;700&display=swap">
<style>
  :root {
    --page-bg: #d9dcdf;
    --card-bg: #eef0f2;
    --card-edge: #ffffff;
    --ink: #111111;
    --band: #222222;
    --band-text: #ffffff;
    --orange: #f5a623;
    --black: #1a1a1a;
    --blue: #3db7ea;
    --red: #ec2a2f;
    --logo-ink: #2b2b2b;
  }
  * { margin: 0; padding: 0; box-sizing: border-box; }
  html, body {
    width: 1200px; height: 900px; overflow: hidden;
    background: var(--page-bg);
    font-family: "Arimo", Arial, sans-serif;
  }
  .card {
    position: absolute; left: 120px; top: 137px;
    width: 960px; height: 626px;
    background: var(--card-bg);
    border: 2px solid var(--card-edge);
    box-shadow: 0 10px 30px rgba(0,0,0,.18);
    overflow: hidden;
  }
  .pattern { position: absolute; display: block; }
  .pattern--corner { left: 0; top: 0; width: 300px; height: 230px; }
  .pattern--side { right: 0; top: 82px; width: 116px; height: 372px; }

  .brand {
    position: absolute; left: 419px; top: 44px;
    display: flex; align-items: center; gap: 16px;
  }
  .brand__mark { width: 100px; height: 100px; background: var(--orange); }
  .brand__name {
    font-size: 35px; font-weight: 400; color: var(--logo-ink);
    letter-spacing: .5px; text-transform: uppercase; white-space: nowrap;
  }

  .contacts { position: absolute; left: 0; top: 362px; list-style: none; }
  .contact { display: flex; align-items: center; height: 34px; margin-bottom: 18px; }
  .contact__icon { width: 100px; height: 34px; flex: none; }
  .contact__text {
    margin-left: 24px; font-size: 25px; font-weight: 700; color: var(--ink);
    letter-spacing: .5px; text-transform: uppercase; white-space: nowrap;
  }

  .services {
    position: absolute; left: 0; right: 0; top: 561px; height: 56px;
    background: var(--band); color: var(--band-text);
    display: flex; align-items: center; justify-content: center;
    font-size: 26px; font-weight: 700; letter-spacing: 1px;
  }
</style>
</head>
<body>
  <main class="card">
    <svg class="pattern pattern--corner" viewBox="0 0 300 230" role="img" aria-label="Orange and black triangle mosaic pattern">
      <defs>
        <linearGradient id="cornerTone" x1="0" y1="0" x2="1" y2="1">
          <stop offset="0" stop-color="#f5a623"/>
          <stop offset=".45" stop-color="#1a1a1a"/>
          <stop offset="1" stop-color="#f5a623"/>
        </linearGradient>
      </defs>
      <polygon points="0,0 290,0 230,110 150,230 0,230" fill="url(#cornerTone)"/>
    </svg>

    <svg class="pattern pattern--side" viewBox="0 0 116 372" role="img" aria-label="Black and orange triangle mosaic pattern">
      <defs>
        <linearGradient id="sideTone" x1="0" y1="0" x2="0" y2="1">
          <stop offset="0" stop-color="#1a1a1a"/>
          <stop offset=".4" stop-color="#1a1a1a"/>
          <stop offset=".55" stop-color="#f5a623"/>
          <stop offset="1" stop-color="#f5a623"/>
        </linearGradient>
      </defs>
      <polygon points="116,0 116,372 60,290 0,190 60,100" fill="url(#sideTone)"/>
    </svg>

    <header class="brand">
      <span class="brand__mark" aria-hidden="true"></span>
      <h1 class="brand__name">Tolvane Electrical</h1>
    </header>

    <ul class="contacts">
      <li class="contact">
        <svg class="contact__icon" viewBox="0 0 100 34" aria-hidden="true">
          <rect x="0" y="2" width="50" height="30" fill="var(--blue)"/>
          <rect x="56" y="0" width="34" height="34" fill="var(--blue)"/>
          <polygon points="90,12 98,17 90,22" fill="var(--blue)"/>
          <circle cx="73" cy="12" r="6" fill="#fff"/>
          <path d="M62 30 Q62 19 73 19 Q84 19 84 30 Z" fill="#fff"/>
        </svg>
        <span class="contact__text">Gareth Pomfrey</span>
      </li>
      <li class="contact">
        <svg class="contact__icon" viewBox="0 0 100 34" aria-hidden="true">
          <rect x="0" y="2" width="50" height="30" fill="var(--orange)"/>
          <rect x="56" y="0" width="34" height="34" fill="var(--orange)"/>
          <polygon points="90,12 98,17 90,22" fill="var(--orange)"/>
          <path d="M65 8 L70 7 L72 13 L69 15 Q71 21 76 24 L78 21 L84 23 L83 28 Q80 30 75 28 Q66 23 64 13 Z" fill="#fff"/>
        </svg>
        <span class="contact__text">0437 519 284</span>
      </li>
      <li class="contact">
        <svg class="contact__icon" viewBox="0 0 100 34" aria-hidden="true">
          <rect x="0" y="2" width="50" height="30" fill="var(--red)"/>
          <rect x="56" y="0" width="34" height="34" fill="var(--red)"/>
          <polygon points="90,12 98,17 90,22" fill="var(--red)"/>
          <text x="73" y="25" text-anchor="middle" font-family="Arimo, Arial, sans-serif" font-size="22" font-weight="700" fill="#fff">@</text>
        </svg>
        <span class="contact__text">gareth@tolvaneelectrical.com.au</span>
      </li>
    </ul>

    <footer class="services">ELECTRICAL - COMMUNICATIONS - AUDIO - VISUAL</footer>
  </main>
</body>
</html>
```